Business Card Design Project

Please create a custom business card for Loftwell Capital. The logo is attached to this brief.

Also, here is the link to the logo design project: http://jobs.briskmotif.com/job.aspx?id=462035

Questions can be posted on the Discussion Board.

```html
<!DOCTYPE html>
<html lang="en">
<head>
<meta charset="utf-8">
<title>Loftwell Capital – Business Cards</title>
<link rel="stylesheet" href="https://fonts.googleapis.com/css2?family=Open+Sans:wght@400;600;700&family=Montserrat:wght@400&display=swap">
<style>
  :root {
    --backdrop: #e4e5e7;
    --card-white: #ffffff;
    --card-dark: #3a3a3c;
    --navy: #263a7a;
    --brand-blue: #2f86d1;
    --ink: #3b3b3d;
    --rule: #9a9a9a;
    --text-light: #f4f4f4;
  }
  * { margin: 0; padding: 0; box-sizing: border-box; }
  html, body { width: 1200px; height: 904px; overflow: hidden; }
  body {
    background: var(--backdrop);
    font-family: "Open Sans", Arial, sans-serif;
    color: var(--ink);
    position: relative;
  }
  .card {
    position: absolute;
    top: 300px;
    width: 520px;
    height: 300px;
    border-radius: 3px;
    box-shadow: 0 6px 18px rgba(0,0,0,.18);
    overflow: hidden;
  }
  /* Front */
  .card-front { left: 50px; background: var(--card-white); }
  .front-identity {
    position: absolute; left: 34px; top: 40px;
  }
  .person-name { font-size: 22px; font-weight: 700; color: var(--navy); line-height: 1.1; }
  .person-title { font-size: 13px; color: var(--ink); margin-top: 2px; }
  .front-brand {
    position: absolute; right: 34px; top: 44px;
    display: flex; align-items: center; gap: 10px;
    font-family: "Montserrat", Arial, sans-serif;
    font-size: 22px; letter-spacing: 3px; text-transform: uppercase; color: var(--ink);
  }
  .brand-square { width: 16px; height: 16px; background: var(--brand-blue); flex: none; }
  .divider {
    position: absolute; left: 34px; right: 34px; top: 120px;
    height: 1px; background: var(--rule);
  }
  .contact-list {
    position: absolute; left: 34px; top: 140px;
    list-style: none; font-size: 13px; line-height: 20px;
  }
  .contact-list li { display: flex; align-items: center; gap: 10px; }
  .contact-list svg { width: 13px; height: 13px; fill: var(--navy); flex: none; }
  .address {
    position: absolute; right: 34px; top: 140px;
    text-align: right; font-size: 13px; line-height: 20px; font-style: normal;
  }
  .address-company { font-weight: 700; color: var(--navy); text-transform: uppercase; }
  .front-band { position: absolute; right: 0; bottom: 0; width: 200px; height: 44px; }
  /* Back */
  .card-back {
    left: 630px; background: var(--card-dark);
    display: flex; align-items: center; justify-content: center;
  }
  .back-brand {
    display: flex; align-items: center; gap: 16px;
    font-family: "Montserrat", Arial, sans-serif;
    font-size: 34px; letter-spacing: 5px; text-transform: uppercase; color: var(--text-light);
  }
  .back-brand .brand-square { width: 26px; height: 26px; }
</style>
</head>
<body>
  <section class="card card-front" aria-label="Business card front">
    <div class="front-identity">
      <p class="person-name">Martin Hale</p>
      <p class="person-title">Director</p>
    </div>
    <div class="front-brand"><span class="brand-square"></span>Loftwell Capital</div>
    <div class="divider"></div>
    <ul class="contact-list">
      <li><svg viewBox="0 0 16 16"><path d="M3 1l3 3-2 2c1 2 4 5 6 6l2-2 3 3-2 2C7 15 1 9 1 3z"/></svg>555 014 2238</li>
      <li><svg viewBox="0 0 16 16"><rect x="4" y="1" width="8" height="14" rx="1.5"/></svg>555 014 2238</li>
      <li><svg viewBox="0 0 16 16"><path d="M1 3h14v10H1z M1 3l7 6 7-6" fill="none" stroke="#263a7a" stroke-width="1.6"/></svg>info@loftwellcapital.co.uk</li>
      <li><svg viewBox="0 0 16 16"><circle cx="8" cy="8" r="6.5" fill="none" stroke="#263a7a" stroke-width="1.5"/><path d="M1.5 8h13M8 1.5c-3 3.5-3 9.5 0 13M8 1.5c3 3.5 3 9.5 0 13" fill="none" stroke="#263a7a" stroke-width="1.2"/></svg>www.loftwellcapital.co.uk</li>
    </ul>
    <address class="address">
      <span class="address-company">Loftwell Capital</span><br>
      Suite 48, Ashmore Street,<br>
      Opposite Riverside Park, Kenton,<br>
      NY 10482
    </address>
    <svg class="front-band" viewBox="0 0 200 44" preserveAspectRatio="none" aria-hidden="true">
      <path d="M0 44V14h10l8-14h182v44z" fill="#263a7a"/>
    </svg>
  </section>

  <section class="card card-back" aria-label="Business card back">
    <div class="back-brand"><span class="brand-square"></span>Loftwell Capital</div>
  </section>
</body>
</html>
```